Background on the company
=======================
This is a Bitcoin Consulting Company.

We have two projects.

Tinted Tokens: software to trade assets over the Bitcoin protocol (assets like property, traditional currencies, gold, stocks, securities, bonds, etc.).

Vaultrix Home Teller: a hardware based web service in a box that manages cold storage wallets and off line transaction signing. It is the secure way to deploy a web wallet without relying on third parties.

All that to say this is a high tech company focusing on Bitcoin.

What does Drellowmar mean?
========================

The Beast of Drellowmar is the rabbit in Quimby Larkets's Silver Goblet that defeats his band of knights. (At least until they go and get the Holy Hand Grenade).

We like this, because we are a deceptively soft and fuzzy company that is also killer!

What We Need:
============

Primarily we need to get the logo designed. I have a hand drawing I did, but you are not limited to that. And the logo needs to work on a business card. The right logo that works on a Business Card is the primary consideration.
Updates

The main task here is to get the logo right.  I have provided a drawing I made, and I like it, but my complaints are:  Drellowmar is hard to read.  The 'C' isn't obvious.

We can fix this many ways.  We can forget the whole "combinde a rabit with the C and a" idea.  We can add "Drellowmar Systems" on the card apart from the logo (that way if they don't "get it" they can still read it.)

The Rabbit itself is quite obviously scanned from a hand drawing.  That might not be a bad thing, but combine that with the entire logo, and it is too cheap looking.

Target Market(s)

Technical folks. Investors. Business contacts.

Industry/Entity Type

Software

Requirements
Must have
• We have to clean up the logo, or replace it with something that hints at the same sort of things. (See the upload) Basically and innocent white bunny. Something that works on a Business Card.

All the information below:

Derek Hale
ph (555) 314-9072
hale.derek@mailvora.net
derek@drellowmar.net
Nice to have
• I would like it to be serious, yet whimsical. An inside joke, so you get it if you know Quimby Larkets. But otherwise, it looks reasonably serious if you don't know Quimby Larkets.

I don't want it to be scary. (oddly, that my own efforts seem to make that easy to do)

Would like a set of colors that remind one of a cave, a rabbit, knights.... Not sure what those are...

```html
<!DOCTYPE html>
<html lang="en">
<head>
<meta charset="utf-8">
<title>Drellowmar Business Card</title>
<link rel="stylesheet" href="https://fonts.googleapis.com/css2?family=Arimo:wght@400;700&display=swap">
<style>
  :root {
    --backdrop: #e4e4e4;
    --card: #ffffff;
    --ink: #1c1c1c;
    --accent: #e3262b;
    --stripe-dark: #1f1f1f;
  }
  html, body {
    margin: 0;
    padding: 0;
    width: 1200px;
    height: 900px;
    overflow: hidden;
    background: var(--backdrop);
  }
  .business-card {
    position: absolute;
    left: 100px;
    top: 164px;
    width: 1000px;
    height: 572px;
    background: var(--card);
    border-radius: 44px;
    overflow: hidden;
    font-family: "Arimo", Arial, sans-serif;
    color: var(--ink);
    box-shadow: 0 10px 30px rgba(0,0,0,0.12);
  }
  .holder-name {
    position: absolute;
    top: 52px;
    right: 66px;
    margin: 0;
    font-size: 30px;
    font-weight: 400;
    color: var(--accent);
  }
  .brand {
    position: absolute;
    top: 200px;
    left: 0;
    width: 100%;
    display: flex;
    justify-content: center;
    align-items: center;
    gap: 22px;
  }
  .brand-dot {
    width: 34px;
    height: 34px;
    border-radius: 50%;
    background: var(--accent);
  }
  .brand-name {
    margin: 0;
    font-size: 84px;
    font-weight: 700;
    color: var(--ink);
    letter-spacing: -1px;
  }
  .contact-list {
    position: absolute;
    left: 78px;
    top: 378px;
    margin: 0;
    padding: 0;
    list-style: none;
    font-size: 36px;
    line-height: 50px;
  }
  .contact-item {
    display: flex;
    align-items: center;
    gap: 12px;
  }
  .contact-icon {
    width: 34px;
    height: 34px;
    flex: none;
  }
  .corner-stripes {
    position: absolute;
    inset: 0;
    width: 100%;
    height: 100%;
    pointer-events: none;
  }
</style>
</head>
<body>
  <div class="business-card">
    <svg class="corner-stripes" viewBox="0 0 1000 572" aria-hidden="true">
      <line x1="1060" y1="290" x2="640" y2="600" stroke="var(--stripe-dark)" stroke-width="13"/>
      <line x1="1060" y1="322" x2="690" y2="600" stroke="var(--accent)" stroke-width="11"/>
      <line x1="1060" y1="352" x2="740" y2="600" stroke="var(--accent)" stroke-width="6"/>
    </svg>

    <p class="holder-name">Derek Hale</p>

    <div class="brand">
      <span class="brand-dot"></span>
      <p class="brand-name">Drellowmar</p>
    </div>

    <ul class="contact-list">
      <li class="contact-item">
        <svg class="contact-icon" viewBox="0 0 24 24" aria-hidden="true">
          <path fill="var(--accent)" d="M6.6 10.8a15.1 15.1 0 0 0 6.6 6.6l2.2-2.2c.3-.3.7-.4 1-.2 1.1.4 2.3.6 3.6.6.6 0 1 .4 1 1V20c0 .6-.4 1-1 1A17 17 0 0 1 3 4c0-.6.4-1 1-1h3.5c.6 0 1 .4 1 1 0 1.3.2 2.5.6 3.6.1.3 0 .7-.2 1z"/>
        </svg>
        <span>(555) 314-9072</span>
      </li>
      <li class="contact-item">
        <svg class="contact-icon" viewBox="0 0 24 24" aria-hidden="true">
          <rect x="2" y="5" width="20" height="14" rx="1.5" fill="var(--accent)"/>
          <path d="M3 6.5l9 6.5 9-6.5" fill="none" stroke="#ffffff" stroke-width="1.6"/>
        </svg>
        <span>hale.derek@mailvora.net</span>
      </li>
      <li class="contact-item">
        <svg class="contact-icon" viewBox="0 0 24 24" aria-hidden="true">
          <rect x="2" y="5" width="20" height="14" rx="1.5" fill="var(--accent)"/>
          <path d="M3 6.5l9 6.5 9-6.5" fill="none" stroke="#ffffff" stroke-width="1.6"/>
        </svg>
        <span>derek@drellowmar.net</span>
      </li>
    </ul>
  </div>
</body>
</html>
```